New look and feel for a Website, mobile design, desktop design

We do a redesign of the website quonbath.com. We expect the designer to come up with ideas about a new look AND feel.
Starting point of the designers considerations should be the mobile design. Even though we are not creating a mobile App, the designer should think of it as one regarding design and usability. Using responsive design technology, we will shift from the mobile design to the desktop design and likewise. So the designer is supposed to come up with a solution for that as well.
What we expect
- definition of single design-elements that can be used in various places
- creation of a mobile design for all different types of pages
- creation of a desktop design for all different types of pages
Find a detailed description in the redesign-specification.

Target Market(s)

Germany, Austria, Switzerland

Industry/Entity Type

Residential Construction

Number of Pages Required

5+ page

Font styles to use
Other font styles liked:
• Open Sans

Colors

Designer to choose colors to be used in the design.

Requirements
Must have
• - mobile design concept
• - desktop design concept

```html
<!DOCTYPE html>
<html lang="en">
<head>
<meta charset="utf-8">
<title>quonbath – A new bath in 24 hours</title>
<link rel="stylesheet" href="https://fonts.googleapis.com/css2?family=Open+Sans:wght@400;600;700&family=Roboto+Condensed:wght@300;400&display=swap">
<style>
:root{
  --orange:#ef6c1c;
  --teal-1:#41c7a8;
  --teal-2:#21a48a;
  --blue:#1b72b9;
  --blue-band:#1a74b9;
  --ink:#222;
  --muted:#666;
  --grey-bg:#f0f0f0;
  --footer:#141414;
  --footer-base:#050505;
  --white:#fff;
}
*{box-sizing:border-box;margin:0;padding:0}
html,body{width:1200px;height:3051px;overflow:hidden}
body{font-family:"Open Sans",Arial,sans-serif;color:var(--ink);background:var(--white);position:relative}
.abs{position:absolute}
.top-line{top:0;left:0;width:1200px;height:8px;background:var(--orange)}
.header{top:8px;left:0;width:1200px;height:104px}
.brand{left:96px;top:20px;display:flex;flex-direction:column;align-items:center;gap:6px}
.brand-dot{width:44px;height:44px;border-radius:50%;background:var(--blue)}
.brand-name{font-size:24px;font-weight:600;color:var(--blue);line-height:1}
.call-label{left:635px;top:40px;font-size:17px;color:#333}
.phone-select{left:793px;top:37px;width:194px;height:36px;border:1px solid #ccc;border-radius:3px;display:flex;align-items:center;padding-left:10px;font-size:17px;color:#222;gap:10px}
.flag{width:26px;height:16px;background:linear-gradient(#e5202e 0 33%,#fff 33% 67%,#e5202e 67%)}
.caret{width:0;height:0;border-left:6px solid transparent;border-right:6px solid transparent;border-top:7px solid #222;margin-left:4px}
.btn-contact{left:1003px;top:35px;width:107px;height:37px;background:var(--blue);color:#fff;font-size:17px;display:flex;align-items:center;justify-content:center;border-radius:2px}
.nav{top:112px;left:0;width:1200px;height:56px;background:linear-gradient(var(--teal-1),var(--teal-2))}
.nav a{position:absolute;top:16px;color:#fff;font-size:17px;text-decoration:none}
.hero{top:168px;left:0;width:1200px;height:507px;background:linear-gradient(100deg,#8c8c8c 0%,#b7b5b3 28%,#6d3a3c 55%,#8b1f2a 70%,#d8d6d4 100%)}
.hero-title{left:88px;top:150px;font-size:52px;font-weight:700;color:#fff;letter-spacing:1px;line-height:62px}
.hero-sub{left:88px;top:220px;font-size:22px;color:#fff;line-height:31px;width:400px}
.btn-consult{left:92px;top:300px;width:284px;height:37px;background:var(--blue);color:#fff;font-size:17px;display:flex;align-items:center;justify-content:center}
.slide-dot{top:360px;width:24px;height:24px;border-radius:50%;background:#444;display:flex;align-items:center;justify-content:center}
.area-panel{left:765px;top:131px;width:346px;height:244px;background:rgba(0,0,0,.82);color:#fff;text-align:center}
.area-title{margin-top:28px;font-size:25px}
.area-input{position:absolute;left:32px;top:78px;width:281px;height:45px;background:#fff;color:#333;font-size:15px;display:flex;align-items:center;padding-left:14px;gap:8px}
.area-or{position:absolute;left:0;width:100%;top:125px;font-size:20px}
.btn-partner{position:absolute;left:32px;top:158px;width:281px;height:44px;background:var(--orange);color:#fff;font-size:16px;display:flex;align-items:center;justify-content:center}
.section-title{font-family:"Roboto Condensed",Arial,sans-serif;font-weight:400;font-size:33px;color:#111;text-align:center;width:1200px;left:0}
.section-sub{width:1200px;left:0;text-align:center;font-size:17px;color:#555}
.offer-card{top:875px;width:401px;height:230px;border:1px solid #bbb;box-shadow:0 2px 6px rgba(0,0,0,.25);background:#fff;text-align:center}
.offer-label{display:flex;align-items:center;justify-content:center;gap:12px;margin-top:62px;height:40px}
.offer-square{width:22px;height:22px;background:var(--orange)}
.offer-name{font-size:26px;font-weight:600;color:var(--orange);line-height:1}
.offer-text{position:absolute;left:0;width:100%;top:160px;font-size:14px;color:#222;line-height:22px;padding:0 24px}
.recs{top:1190px;left:0;width:1200px;height:600px;background:var(--grey-bg)}
.rec-card{top:1349px;width:311px;height:281px;background:#fff;box-shadow:0 2px 5px rgba(0,0,0,.18);text-align:center}
.rec-photo{height:167px;width:100%}
.rec-name{font-size:17px;color:#222;line-height:24px;margin-top:18px}
.read-more{font-size:14px;color:#e9433c}
.btn-all{left:484px;top:1676px;width:232px;height:49px;border:1px solid #444;border-radius:3px;font-size:17px;display:flex;align-items:center;justify-content:center;background:#fafafa}
.interviews{top:1790px;left:0;width:1200px;height:482px;background:linear-gradient(90deg,#1766a8,var(--blue-band) 50%,#1d80c6)}
.interview-card{left:148px;top:1877px;width:900px;height:326px;background:#fff;box-shadow:0 4px 12px rgba(0,0,0,.3)}
.iv-title{left:40px;top:34px;font-size:26px;font-weight:400;color:#222}
.iv-sub{left:40px;top:80px;font-size:18px;color:#333}
.iv-text{left:40px;top:128px;width:430px;font-size:14px;line-height:23px;color:#444;text-align:justify}
.btn-view{left:41px;top:255px;width:108px;height:32px;border-radius:16px;background:var(--orange);color:#fff;font-size:12px;font-weight:700;display:flex;align-items:center;justify-content:center}
.iv-media{left:507px;top:0;width:393px;height:326px;background:linear-gradient(135deg,#e9e6e2,#c8c2bc 50%,#d46a2a 75%,#b84c1d)}
.play{left:150px;top:120px}
.arrow-btn{top:2006px;width:56px;height:56px;border-radius:50%;background:rgba(255,255,255,.35);display:flex;align-items:center;justify-content:center}
.article{top:2376px;width:313px}
.article-photo{height:173px;width:100%}
.article-title{font-size:15px;font-weight:400;color:#222;margin-top:28px}
.article-text{font-size:12.5px;color:#777;line-height:20px;margin-top:8px}
.article .read-more{display:block;margin-top:6px;font-size:13px;color:#ef6c3c}
.footer{top:2752px;left:0;width:1200px;height:218px;background:var(--footer);color:#fff}
.footer-brand{left:92px;top:58px;display:flex;flex-direction:column;align-items:center;gap:8px}
.footer-brand .brand-dot{background:#fff}
.footer-brand .brand-name{color:#fff;font-size:28px}
.f-head{top:52px;font-size:14px;letter-spacing:.5px}
.f-body{font-size:11.5px;line-height:22px;color:#ddd}
.f-body b{font-size:15px;font-weight:400;color:#fff}
.nl-input{left:643px;top:130px;width:146px;height:29px;background:#fff;color:#888;font-size:11px;padding-left:8px;display:flex;align-items:center}
.nl-submit{left:789px;top:130px;width:55px;height:29px;background:var(--orange);color:#fff;font-size:11px;display:flex;align-items:center;justify-content:center}
.social{top:96px;width:26px;height:26px;border-radius:4px;background:#fff}
.base{top:2970px;left:0;width:1200px;height:81px;background:var(--footer-base);color:#fff;font-size:13px;text-align:center;line-height:81px}
.chat{left:995px;top:3012px;width:118px;height:39px;background:var(--orange);color:#fff;font-size:16px;border-radius:4px 4px 0 0;display:flex;align-items:center;justify-content:center;gap:6px}
</style>
</head>
<body>

<div class="abs top-line"></div>

<header class="abs header">
  <div class="abs brand"><span class="brand-dot"></span><span class="brand-name">quonbath</span></div>
  <div class="abs call-label">Call now for free :</div>
  <div class="abs phone-select"><span class="flag"></span>0800 41 63 57<span class="caret"></span></div>
  <div class="abs btn-contact">Contact</div>
</header>

<nav class="abs nav">
  <a style="left:118px">Bath solutions</a>
  <a style="left:272px">Bath information</a>
  <a style="left:447px">Measure up</a>
  <a style="left:584px">Customer opinions</a>
  <a style="left:773px">Locations</a>
  <a style="left:891px">Press</a>
  <a style="left:976px">About quonbath</a>
</nav>

<section class="abs hero" role="img" aria-label="Photo of a renovated bathroom with walk-in shower and red tiled wall">
  <h1 class="abs hero-title">QUONBATH</h1>
  <p class="abs hero-sub">Neque porro quisquam est qui dolorem ipsum quia doloramet</p>
  <div class="abs btn-consult">Request for a free consultation</div>
  <div class="abs slide-dot" style="left:96px"><svg width="10" height="10" viewBox="0 0 10 10"><path d="M7 1 3 5l4 4" stroke="#fff" stroke-width="2" fill="none"/></svg></div>
  <div class="abs slide-dot" style="left:124px"><svg width="10" height="10" viewBox="0 0 10 10"><path d="M3 1l4 4-4 4" stroke="#fff" stroke-width="2" fill="none"/></svg></div>
  <div class="abs area-panel">
    <div class="area-title">Quonbath in your area</div>
    <div class="area-input"><svg width="12" height="12" viewBox="0 0 12 12"><circle cx="5" cy="5" r="3.5" stroke="#333" stroke-width="1.6" fill="none"/><path d="M7.5 7.5 11 11" stroke="#333" stroke-width="1.8"/></svg>PLZ eingeben</div>
    <div class="area-or">or</div>
    <div class="btn-partner">Switch to the partner overview</div>
  </div>
</section>

<h2 class="abs section-title" style="top:736px">A NEW BATH IN 24 HOURS</h2>
<p class="abs section-sub" style="top:788px">with quonbath system solutions for bathroom renovation</p>

<div class="abs offer-card" style="left:175px">
  <div class="offer-label"><span class="offer-square"></span><span class="offer-name">BathRenew</span></div>
  <p class="offer-text">A new bathroom, barrier-free and senior-friendly!<br>And that within 24 working hours!</p>
</div>
<div class="abs offer-card" style="left:614px">
  <div class="offer-label"><span class="offer-square"></span><span class="offer-name">ShowerRenew</span></div>
  <p class="offer-text" style="top:171px">Get out, shower in! Or just a new shower within a day!</p>
</div>

<section class="abs recs"></section>
<h2 class="abs section-title" style="top:1252px">RECOMMENDATIONS</h2>

<article class="abs rec-card" style="left:116px">
  <div class="rec-photo" role="img" aria-label="Photo of a glass shower with grey wall panels" style="background:linear-gradient(90deg,#5d7a74,#8fa7a0 50%,#d9d6cf)"></div>
  <p class="rec-name">Recommendation of<br>the Lindholm family</p>
  <span class="read-more">Read More »</span>
</article>
<article class="abs rec-card" style="left:452px">
  <div class="rec-photo" role="img" aria-label="Photo of a bright walk-in shower" style="background:linear-gradient(90deg,#cfd3d6,#eef0f1 50%,#bfc5c9)"></div>
  <p class="rec-name">Recommendation of<br>Mr. Brandel</p>
  <span class="read-more">Read More »</span>
</article>
<article class="abs rec-card" style="left:791px">
  <div class="rec-photo" role="img" aria-label="Photo of a bathroom with red shower wall and washbasin" style="background:linear-gradient(90deg,#b3303a,#e8e2dc 50%,#c9bdb5)"></div>
  <p class="rec-name">Recommendation of<br>Ms. Korvin</p>
  <span class="read-more">Read More »</span>
</article>
<div class="abs btn-all">All recommendations</div>

<section class="abs interviews"></section>
<div class="abs arrow-btn" style="left:75px"><svg width="18" height="22" viewBox="0 0 18 22"><path d="M13 2 4 11l9 9" stroke="#fff" stroke-width="2.5" fill="none"/></svg></div>
<div class="abs arrow-btn" style="left:1070px"><svg width="18" height="22" viewBox="0 0 18 22"><path d="M5 2l9 9-9 9" stroke="#fff" stroke-width="2.5" fill="none"/></svg></div>
<article class="abs interview-card">
  <h3 class="abs iv-title">Customer Interviews</h3>
  <p class="abs iv-sub">Rebuilding by family Hallberg from Ostfeld</p>
  <p class="abs iv-text">By replacing the old bathtub with a new floor-level shower, Mr. and Mrs. Hallberg can now take a relaxed shower. Shower walls were mounted over the old wall tiles. So mold formation has no chance! To modernize this way Hallbergs brought the luxury of a quiet and clean conversion.</p>
  <div class="abs btn-view">VIEW MORE</div>
  <div class="abs iv-media" role="img" aria-label="Video still of a customer in her new bathroom">
    <svg class="abs play" width="64" height="64" viewBox="0 0 64 64"><circle cx="32" cy="32" r="32" fill="rgba(60,40,35,.75)"/><path d="M25 19v26l21-13z" fill="#fff"/></svg>
  </div>
</article>

<article class="abs article" style="left:96px">
  <div class="article-photo" role="img" aria-label="Photo of a bathroom exhibition room" style="background:linear-gradient(90deg,#d8d4cc,#f1efe9 45%,#a9c44a 75%,#d9d6cf)"></div>
  <h4 class="article-title">The bathroom exhibition in your area</h4>
  <p class="article-text">It has survived not only five centuries, but also the leap into electronic typesetting.</p>
  <span class="read-more">Read More »</span>
</article>
<article class="abs article" style="left:443px">
  <div class="article-photo" role="img" aria-label="Photo of a bathroom planner advising customers at a table" style="background:linear-gradient(90deg,#8a7660,#c7b7a0 45%,#6d8fb8 75%,#ddd6cb)"></div>
  <h4 class="article-title">The bathroom planner who comes</h4>
  <p class="article-text">It has survived not only five centuries, but also the leap into electronic typesetting.</p>
  <span class="read-more">Read More »</span>
</article>
<article class="abs article" style="left:797px">
  <div class="article-photo" role="img" aria-label="Photo of a small bathroom with orange wall and glass shower" style="background:linear-gradient(90deg,#9b8d80,#d7d1c9 40%,#d9622a 75%,#e8e3dc)"></div>
  <h4 class="article-title">Set up small bathrooms</h4>
  <p class="article-text">It has survived not only five centuries, but also the leap into electronic typesetting.</p>
  <span class="read-more">Read More »</span>
</article>

<footer class="abs footer">
  <div class="abs footer-brand"><span class="brand-dot"></span><span class="brand-name">quonbath</span></div>
  <div class="abs f-head" style="left:323px">CONTACT US</div>
  <div class="abs f-body" style="left:323px;top:86px">
    Address : 48 Harbor Lane, Suite 12<br>
    Millbrook, Oregon 97000, United States<br>
    Phone : <b>555-301-4820</b><br>
    Email : hello@quonbath.com
  </div>
  <div class="abs f-head" style="left:641px">SIGN UP FOR NEWSLETTER</div>
  <div class="abs f-body" style="left:643px;top:84px;width:210px;line-height:17px">Your about us information would fit here nicely.</div>
  <div class="abs nl-input">Email address</div>
  <div class="abs nl-submit">Submit</div>
  <div class="abs f-head" style="left:946px">FOLLOW US OUT THERE</div>
  <span class="abs social" style="left:948px"></span>
  <span class="abs social" style="left:984px"></span>
  <span class="abs social" style="left:1020px"></span>
  <span class="abs social" style="left:1056px"></span>
</footer>

<div class="abs base">Copyright © 2018. All Rights Reserved</div>
<div class="abs chat"><svg width="16" height="14" viewBox="0 0 16 14"><path d="M2 1h12a1 1 0 0 1 1 1v7a1 1 0 0 1-1 1H7l-4 3v-3H2a1 1 0 0 1-1-1V2a1 1 0 0 1 1-1z" fill="#fff"/></svg>Chat Now</div>

</body>
</html>
```